2 Creative Website Banners for Furniture Brand

Morning Tobrasca....
The get a great night sleep banner is complete - we are happy with that one.
Ive uploaded a slightly different concept for the other banner below. This is just something rough ive thrown together. But you can see I have added a curve, a maroon coloured background which is slightly transparent and a big heart in the background....
I do not necessarily want to use this heart image but something a bit like this (a nice graphic, gif etc) but something quite elegant faded in, or perhaps a number of hearts (done in a tasteful way). Also can we keep the typography in the same format as you can see for this one.
Nearly there :)!
Industry/Entity Type
Furniture

```html
<!DOCTYPE html>
<html lang="en">
<head>
<meta charset="utf-8">
<title>Harrowmere Furniture</title>
<link rel="stylesheet" href="https://fonts.googleapis.com/css2?family=Montserrat:wght@200;300;400;500&display=swap">
<style>
  :root {
    --notice-bg: #e0d8c8;
    --notice-text: #a08a3c;
    --header-bg: #ffffff;
    --brand: #3a1f3a;
    --ink: #2b2530;
    --gold: #c9a93a;
    --nav-bg: #a69081;
    --nav-text: #ffffff;
    --maroon: #4a1a2c;
    --hero-text: #ffffff;
    --flag-blue: #24336b;
  }
  * { margin: 0; padding: 0; box-sizing: border-box; }
  html, body { width: 1200px; height: 517px; overflow: hidden; background: #fff; }
  body { font-family: "Montserrat", sans-serif; position: relative; }

  .notice-bar {
    position: absolute; left: 0; top: 0; width: 1200px; height: 23px;
    background: var(--notice-bg); color: var(--notice-text);
    font-size: 10.5px; letter-spacing: 0.2px; text-align: center; line-height: 23px;
  }

  .site-header {
    position: absolute; left: 0; top: 23px; width: 1200px; height: 97px;
    background: var(--header-bg);
  }
  .brand-name {
    position: absolute; left: 50px; top: 28px;
    font-size: 26px; font-weight: 400; letter-spacing: 2.5px; color: var(--brand);
  }
  .phone {
    position: absolute; left: 941px; top: 11px; display: flex; align-items: center; gap: 12px;
    font-size: 24px; font-weight: 400; color: var(--ink); letter-spacing: 0.3px;
  }
  .phone-badge { width: 23px; height: 23px; border-radius: 50%; background: var(--flag-blue); }
  .account-links {
    position: absolute; left: 845px; top: 64px; display: flex; gap: 16px;
    font-size: 11px; color: var(--ink);
  }
  .account-link { display: flex; align-items: center; gap: 5px; }
  .cart-count { font-size: 9px; font-weight: 500; margin-left: 4px; }

  .main-nav {
    position: absolute; left: 0; top: 120px; width: 1200px; height: 39px;
    background: var(--nav-bg);
  }
  .nav-item {
    position: absolute; top: 0; line-height: 39px; color: var(--nav-text);
    font-size: 15px; font-weight: 500; display: flex; align-items: center; gap: 8px;
  }

  .hero { position: absolute; left: 0; top: 159px; width: 1200px; height: 358px; overflow: hidden; }
  .hero-photo {
    position: absolute; left: 0; top: 0; width: 1200px; height: 358px;
    background: linear-gradient(120deg, #3b3236 0%, #4e3f46 40%, #6e5c66 62%, #a2a4ab 85%, #5b5e66 100%);
  }
  .hero-overlay { position: absolute; left: 0; top: 0; }
  .hero-kicker {
    position: absolute; left: 123px; top: 90px; color: var(--hero-text);
    font-size: 24px; font-weight: 300; letter-spacing: 0.5px;
  }
  .hero-kicker-rule { position: absolute; left: 125px; top: 125px; width: 66px; height: 2px; background: var(--hero-text); }
  .hero-title {
    position: absolute; left: 121px; top: 163px; color: var(--hero-text);
    font-size: 34px; font-weight: 200; letter-spacing: 0; white-space: nowrap;
  }
  .hero-title strong { font-weight: 400; }
  .hero-button {
    position: absolute; left: 126px; top: 257px; width: 150px; height: 36px;
    background: #fff; color: #111; font-size: 17px; line-height: 36px; text-align: center;
  }
</style>
</head>
<body>
  <div class="notice-bar">COVID 19 - WE ARE TAKING ORDERS AND DELIVERING AS NORMAL</div>

  <header class="site-header">
    <div class="brand-name">HARROWMERE</div>
    <div class="phone"><span class="phone-badge"></span>0345 210 7789</div>
    <div class="account-links">
      <span class="account-link">
        <svg width="15" height="15" viewBox="0 0 15 15"><circle cx="7.5" cy="7.5" r="6" fill="none" stroke="var(--gold)" stroke-width="2"/></svg>
        TRACK ORDER
      </span>
      <span class="account-link">
        <svg width="17" height="15" viewBox="0 0 17 15"><path d="M8.5 14 L2 7.5 A3.8 3.8 0 0 1 8.5 2.5 A3.8 3.8 0 0 1 15 7.5 Z" fill="var(--gold)"/></svg>
        MY WISHLIST
      </span>
      <span class="account-link">
        <svg width="16" height="18" viewBox="0 0 16 18"><rect x="1.5" y="5" width="13" height="11.5" fill="none" stroke="var(--gold)" stroke-width="1.6"/><path d="M5 5 V3.5 A3 3 0 0 1 11 3.5 V5" fill="none" stroke="var(--gold)" stroke-width="1.6"/></svg>
        CART<span class="cart-count">(0)</span>
      </span>
    </div>
  </header>

  <nav class="main-nav">
    <span class="nav-item" style="left:148px">HOME</span>
    <span class="nav-item" style="left:304px">BEDROOM <svg width="10" height="6" viewBox="0 0 10 6"><path d="M1 1 L5 5 L9 1" fill="none" stroke="#fff" stroke-width="1.6"/></svg></span>
    <span class="nav-item" style="left:508px">LIVING ROOM <svg width="10" height="6" viewBox="0 0 10 6"><path d="M1 1 L5 5 L9 1" fill="none" stroke="#fff" stroke-width="1.6"/></svg></span>
    <span class="nav-item" style="left:737px">DINING ROOM <svg width="10" height="6" viewBox="0 0 10 6"><path d="M1 1 L5 5 L9 1" fill="none" stroke="#fff" stroke-width="1.6"/></svg></span>
    <span class="nav-item" style="left:967px">CONTACT <svg width="10" height="6" viewBox="0 0 10 6"><path d="M1 1 L5 5 L9 1" fill="none" stroke="#fff" stroke-width="1.6"/></svg></span>
  </nav>

  <section class="hero">
    <div class="hero-photo" role="img" aria-label="Bedroom with an upholstered wingback bed, grey bedding, fur throw and mirrored bedside furniture"></div>
    <svg class="hero-overlay" width="1200" height="358" viewBox="0 0 1200 358" aria-hidden="true">
      <path d="M0 0 H600 C690 90 690 268 600 358 H0 Z" fill="var(--maroon)" fill-opacity="0.88"/>
      <path d="M600 0 C690 90 690 268 600 358" fill="none" stroke="#ffffff" stroke-opacity="0.25" stroke-width="1.5"/>
      <path d="M470 300 C330 210 340 80 420 80 C450 80 470 105 470 130 C470 105 490 80 520 80 C600 80 610 210 470 300 Z" fill="#ffffff" fill-opacity="0.05" stroke="#ffffff" stroke-opacity="0.12" stroke-width="1.2"/>
      <path d="M560 82 C530 62 532 36 548 36 C555 36 560 42 560 48 C560 42 565 36 572 36 C588 36 590 62 560 82 Z" fill="#ffffff" fill-opacity="0.07"/>
      <path d="M70 330 C48 315 50 296 62 296 C66 296 70 300 70 304 C70 300 74 296 78 296 C90 296 92 315 70 330 Z" fill="#ffffff" fill-opacity="0.06"/>
      <path d="M40 60 C28 52 29 42 36 42 C38 42 40 44 40 46 C40 44 42 42 44 42 C51 42 52 52 40 60 Z" fill="#ffffff" fill-opacity="0.06"/>
    </svg>
    <div class="hero-kicker">INSPIRATION</div>
    <div class="hero-kicker-rule"></div>
    <div class="hero-title">MADE FOR <strong>DREAMING</strong></div>
    <div class="hero-button">&gt; Discover</div>
  </section>
</body>
</html>
```